Marrowfield Contracting Business Cards

Front of card:

Full Logo
Name
Address
Office Phone
Cell Phone
Email
Website

Back:
Logo Mark in background
List and markets and services performed

```html
<!DOCTYPE html>
<html lang="en">
<head>
<meta charset="utf-8">
<title>Marrowfield Contracting Business Cards</title>
<link rel="stylesheet" href="https://fonts.googleapis.com/css2?family=Montserrat:wght@600&family=Mulish:wght@400;600&family=Roboto:wght@500;700&display=swap">
<style>
  :root {
    --stage: #2b2b2b;
    --card-dark: #242424;
    --card-light: #ffffff;
    --brand-red: #e0262b;
    --brand-grey: #8a8a8a;
    --silver: #a9a9a9;
    --ink: #2a2a2a;
    --ink-light: #d8d8d8;
  }
  * { box-sizing: border-box; margin: 0; padding: 0; }
  html, body { width: 1165px; height: 1200px; overflow: hidden; }
  body {
    background: var(--stage);
    font-family: "Mulish", sans-serif;
    position: relative;
  }
  .card {
    position: absolute;
    left: 232px;
    width: 700px;
    height: 400px;
    overflow: hidden;
    box-shadow: 0 14px 30px rgba(0,0,0,.45);
  }
  .card--back { top: 170px; background: var(--card-dark); }
  .card--front { top: 630px; background: var(--card-light); }

  .wordmark {
    position: absolute;
    display: flex;
    align-items: center;
    gap: 16px;
    font-family: "Montserrat", sans-serif;
    font-weight: 600;
    text-transform: uppercase;
    line-height: 1.05;
  }
  .wordmark__dot { width: 30px; height: 30px; border-radius: 50%; flex: none; }
  .wordmark__name { font-size: 30px; letter-spacing: 2px; }
  .wordmark__name span { display: block; }

  .card--back .wordmark { left: 175px; top: 150px; color: var(--silver); }
  .card--back .wordmark__dot { background: var(--silver); }
  .tagline {
    position: absolute;
    right: 40px;
    bottom: 42px;
    display: flex;
    align-items: center;
    gap: 8px;
    font-size: 13px;
    color: var(--ink-light);
  }
  .tagline::before {
    content: "";
    width: 7px; height: 7px; border-radius: 50%;
    background: var(--brand-red);
  }

  .card--front .wordmark { right: 40px; top: 40px; color: var(--brand-red); }
  .card--front .wordmark__dot { background: var(--brand-red); }
  .contact {
    position: absolute;
    right: 40px;
    top: 190px;
    list-style: none;
    font-size: 17px;
    color: var(--ink);
    line-height: 1.35;
  }
  .contact li { display: flex; align-items: center; gap: 10px; }
  .contact svg { width: 14px; height: 14px; flex: none; }
  .holder {
    position: absolute;
    left: 40px;
    top: 258px;
    color: var(--ink);
  }
  .holder__name {
    font-family: "Roboto", sans-serif;
    font-weight: 700;
    font-size: 24px;
    color: var(--brand-red);
  }
  .holder__role { font-size: 16px; margin-bottom: 20px; }
  .holder__address { font-size: 16px; line-height: 1.35; font-style: normal; }
  .holder-marker {
    position: absolute;
    left: 0; top: 264px;
    width: 14px; height: 36px;
    background: var(--brand-red);
    border-radius: 0 8px 8px 0;
  }
  .footer-band {
    position: absolute;
    left: 0; right: 0; bottom: 0;
    height: 14px;
    display: flex;
  }
  .footer-band__red { flex: 1; background: var(--brand-red); }
  .footer-band__grey { width: 120px; background: var(--brand-grey); }
  .footer-band__end { width: 16px; background: var(--brand-red); }
</style>
</head>
<body>

<section class="card card--back">
  <div class="wordmark">
    <span class="wordmark__dot"></span>
    <div class="wordmark__name"><span>Marrowfield</span><span>Contracting LLC</span></div>
  </div>
  <p class="tagline">List and markets and services performed</p>
</section>

<section class="card card--front">
  <div class="wordmark">
    <span class="wordmark__dot"></span>
    <div class="wordmark__name"><span>Marrowfield</span><span>Contracting LLC</span></div>
  </div>

  <ul class="contact">
    <li><svg viewBox="0 0 14 14"><rect x="3" y="1" width="8" height="12" rx="1.5" fill="none" stroke="#e0262b" stroke-width="1.6"/></svg>+112 5820 4417</li>
    <li><svg viewBox="0 0 14 14"><path d="M3 1l3 3-1.5 1.5c1 2 2.5 3.5 4.5 4.5L10.5 8.5l3 3-2 2C6 13 1 8 1 3z" fill="#e0262b"/></svg>+112 5820 4418</li>
    <li><svg viewBox="0 0 14 14"><rect x="1" y="3" width="12" height="8" fill="#e0262b"/><path d="M1 3l6 5 6-5" fill="none" stroke="#fff" stroke-width="1.2"/></svg>office@marrowfieldco.com</li>
    <li><svg viewBox="0 0 14 14"><circle cx="7" cy="7" r="5.5" fill="none" stroke="#e0262b" stroke-width="1.3"/><path d="M1.5 7h11M7 1.5c-3 3-3 8 0 11M7 1.5c3 3 3 8 0 11" fill="none" stroke="#e0262b" stroke-width="1"/></svg>www.marrowfieldco.com</li>
  </ul>

  <span class="holder-marker"></span>
  <div class="holder">
    <p class="holder__name">Daniel Harlow</p>
    <p class="holder__role">Founder</p>
    <address class="holder__address">2140 Kestrel Bend Road<br>Tennessee 456, United States</address>
  </div>

  <div class="footer-band">
    <span class="footer-band__red"></span>
    <span class="footer-band__grey"></span>
    <span class="footer-band__end"></span>
  </div>
</section>

</body>
</html>
```